Business Card Design

We need a business card design for a new company based in Allen, Texas. (outside of Dallas,Texas) We offer Business Management Solutions to Entrepreneurs, as well as Corporate Businesses. Our product line offers solutions to Image, Branding, Social Media marketing, business development strategies, banking / funding solutions, just to name a few. We would like to see designs that convey strength and confidence. I have attached a sample design of our company name. Designers you may use company name as either: Tovan or Tovan Corporation, depending on the design layout.

Please show alternate color of Black as well.

Industry/Entity Type

Business

Contact Information for Business Card

Tovan Corporation

4862 N. Brisbury Lane, STE 300
Redmont, TX 75492
Office: 512.638.4471
Fax: 512.638.4472

Dr. Louis Brennick
Business Development Director

```html
<!DOCTYPE html>
<html lang="en">
<head>
<meta charset="UTF-8">
<title>Tovan Corporation — Business Card</title>
<link href="https://fonts.googleapis.com/css2?family=Arimo:wght@400;700&display=swap" rel="stylesheet">
<style>
  :root {
    --page: #e4e4e4;
    --card-dark: #222222;
    --card-light: #eeeeee;
    --ink: #1e1e1e;
    --ink-soft: #2a2a2a;
    --paper-line: #f2f2f2;
  }
  * { margin: 0; padding: 0; box-sizing: border-box; }
  html, body { width: 1200px; height: 900px; overflow: hidden; }
  body {
    background: var(--page);
    font-family: "Arimo", Arial, sans-serif;
    position: relative;
  }
  .card {
    position: absolute;
    left: 303px;
    width: 555px;
    border-radius: 22px;
    overflow: hidden;
  }

  /* Front */
  .card-front { top: 28px; height: 358px; background: var(--card-dark); }
  .front-rule-top {
    position: absolute; left: 0; right: 0; top: 72px; height: 3px; background: var(--paper-line);
  }
  .front-rule-bottom {
    position: absolute; left: 0; right: 0; top: 271px; height: 12px;
    display: flex; align-items: center; gap: 6px;
  }
  .front-rule-bottom .rule { flex: 1; height: 3px; background: var(--paper-line); }
  .front-rule-bottom .word {
    color: var(--paper-line); font-size: 20px; letter-spacing: 0.3px; line-height: 1;
  }
  .front-name {
    position: absolute; left: 0; right: 0; top: 134px;
    text-align: center; color: var(--paper-line);
    font-size: 88px; line-height: 1; letter-spacing: 2px;
  }

  /* Back */
  .card-back { top: 403px; height: 324px; background: var(--card-light); }
  .back-rule {
    position: absolute; left: 0; right: 0; top: 66px; height: 3px; background: var(--ink);
  }
  .back-brand {
    position: absolute; left: 40px; width: 226px; top: 142px; text-align: center; color: var(--ink);
  }
  .back-brand .name { font-size: 58px; line-height: 1; letter-spacing: 1px; }
  .back-brand .sub { font-size: 14px; font-weight: 700; margin-top: 28px; letter-spacing: 0.2px; }
  .back-divider {
    position: absolute; left: 277px; top: 100px; width: 3px; height: 159px; background: var(--ink);
  }
  .person { position: absolute; left: 316px; top: 99px; color: var(--ink); }
  .person .full-name { font-size: 17px; letter-spacing: 0.3px; }
  .person .role { font-size: 12.5px; margin-top: 4px; color: var(--ink-soft); }
  .contact-list { position: absolute; left: 316px; top: 153px; list-style: none; }
  .contact-list li {
    display: flex; align-items: center; height: 26px;
    font-size: 14px; color: var(--ink-soft);
  }
  .contact-list svg { width: 18px; height: 14px; margin-right: 12px; fill: var(--ink); }
  .address {
    position: absolute; left: 0; right: 0; top: 298px;
    display: flex; justify-content: center; align-items: center;
    font-size: 14px; color: var(--ink-soft);
  }
  .address svg { width: 15px; height: 15px; fill: var(--ink); margin-right: 3px; }
</style>
</head>
<body>

  <section class="card card-front">
    <div class="front-rule-top"></div>
    <div class="front-name">Tovan</div>
    <div class="front-rule-bottom">
      <span class="rule"></span>
      <span class="word">CORPORATION</span>
      <span class="rule"></span>
    </div>
  </section>

  <section class="card card-back">
    <div class="back-rule"></div>

    <div class="back-brand">
      <div class="name">Tovan</div>
      <div class="sub">CORPORATION</div>
    </div>

    <div class="back-divider"></div>

    <div class="person">
      <div class="full-name">Dr. LOUIS BRENNICK</div>
      <div class="role">Business Development Director</div>
    </div>

    <ul class="contact-list">
      <li>
        <svg viewBox="0 0 18 14"><path d="M1 4c3-3 13-3 16 0l-1 2-3-1V3H5v2L2 6z"/><path d="M4 7h10l2 6H2z"/></svg>
        512.638.4471
      </li>
      <li>
        <svg viewBox="0 0 18 14"><rect x="5" y="0" width="8" height="4"/><rect x="2" y="4" width="14" height="7"/><rect x="5" y="9" width="8" height="5" fill="#eee" stroke="#1e1e1e" stroke-width="1.2"/></svg>
        512.638.4472
      </li>
      <li>
        <svg viewBox="0 0 18 14"><rect x="2" y="2" width="14" height="10"/><path d="M2 2l7 6 7-6" fill="none" stroke="#eee" stroke-width="1.4"/></svg>
        drbrennick@tovanmail.com
      </li>
      <li>
        <svg viewBox="0 0 18 14"><rect x="2" y="2" width="14" height="10"/><path d="M2 2l7 6 7-6" fill="none" stroke="#eee" stroke-width="1.4"/></svg>
        Info@TovanCorp.com
      </li>
      <li>
        <svg viewBox="0 0 22 16" style="width:22px;height:16px;margin-right:8px"><g fill="none" stroke="#1e1e1e" stroke-width="1.3"><circle cx="8" cy="8" r="6.5"/><ellipse cx="8" cy="8" rx="3" ry="6.5"/><path d="M1.5 8h13M3 4.5h10M3 11.5h10"/><circle cx="15" cy="10" r="3"/><path d="M17 12l4 3.5" stroke-width="2"/></g></svg>
        www.TovanCorp.com
      </li>
    </ul>

    <div class="address">
      <svg viewBox="0 0 16 16"><path d="M8 1L1 8h2v7h4v-4h2v4h4V8h2z"/></svg>
      4862 N. Brisbury Lane, STE 300 Redmont, TX 75492
    </div>
  </section>

</body>
</html>
```